Business Card Design

We sell fish products to corporate food companies who then turn these products into final food products for consumers

Industry/Entity Type

Business

Contact Information for Business Card

I need a corporate business card template for a fish products business. We would like it be professional for use in dealing with multi national companies. This company business card template will be used by multiple employees so the following fields must be open to edit (Name, Phone Number and Email address)

```html
<!DOCTYPE html>
<html lang="en">
<head>
<meta charset="utf-8">
<title>Tidewell Seafoods – Business Card</title>
<link href="https://fonts.googleapis.com/css2?family=Roboto:wght@500;700&display=swap" rel="stylesheet">
<style>
  :root {
    --brand-blue: #0f62b0;
    --card-white: #ffffff;
    --icon-green: #8fcf9a;
    --page-bg: #e9ebee;
    --ink-white: #ffffff;
  }
  * { box-sizing: border-box; margin: 0; padding: 0; }
  html, body {
    width: 1200px; height: 1000px; overflow: hidden;
    background: var(--page-bg);
    font-family: "Roboto", Arial, sans-serif;
  }
  .sheet {
    position: relative; width: 1200px; height: 1000px;
    display: flex; justify-content: center; align-items: center; gap: 100px;
  }
  .card {
    position: relative; width: 400px; height: 700px; overflow: hidden;
    box-shadow: 0 6px 20px rgba(0,0,0,.18);
  }
  /* Front */
  .card--front { background: var(--brand-blue); }
  .front-shape { position: absolute; inset: 0; width: 100%; height: 100%; }
  .halftone-field {
    position: absolute; left: 170px; top: 90px; width: 210px; height: 380px;
    background: radial-gradient(ellipse at 45% 45%, rgba(255,255,255,.26), rgba(255,255,255,0) 70%);
  }
  .contact {
    position: absolute; left: 268px; top: 105px;
    transform-origin: top left; transform: rotate(90deg);
    color: var(--ink-white);
    display: flex; flex-direction: column; gap: 10px;
    white-space: nowrap;
  }
  .contact__name { font-weight: 700; font-size: 32px; letter-spacing: 1px; line-height: 1.1; }
  .contact__line { display: flex; align-items: center; gap: 10px; font-weight: 500; line-height: 1.1; }
  .contact__phone { font-size: 24px; }
  .contact__email { font-size: 17px; }
  .contact__icon {
    width: 26px; height: 26px; border-radius: 50%; flex: none;
    background: var(--icon-green);
    display: flex; align-items: center; justify-content: center;
  }
  .brand {
    position: absolute; display: flex; align-items: center; gap: 10px;
    color: var(--brand-blue); font-weight: 700; white-space: nowrap;
  }
  .brand__dot { width: 26px; height: 26px; border-radius: 50%; background: var(--brand-blue); flex: none; }
  .brand--front { left: 120px; top: 600px; font-size: 25px; }
  /* Back */
  .card--back { background: var(--card-white); }
  .back-shape { position: absolute; inset: 0; width: 100%; height: 100%; }
  .brand--back {
    left: 50%; top: 50%; font-size: 38px;
    transform: translate(-50%, -50%) rotate(90deg);
  }
  .brand--back .brand__dot { width: 34px; height: 34px; }
</style>
</head>
<body>
<main class="sheet">
  <section class="card card--front" aria-label="Business card front">
    <svg class="front-shape" viewBox="0 0 400 700" aria-hidden="true">
      <polygon points="0,700 0,660 250,390 400,560 400,700" fill="var(--card-white)"/>
    </svg>
    <div class="halftone-field" role="img" aria-label="Halftone dot pattern in light blue"></div>
    <div class="contact">
      <p class="contact__name">DANIEL ORWELL</p>
      <p class="contact__line contact__phone">
        <span class="contact__icon">
          <svg width="15" height="15" viewBox="0 0 24 24" aria-hidden="true"><path fill="#fff" d="M6.6 10.8a15.1 15.1 0 006.6 6.6l2.2-2.2c.3-.3.7-.4 1-.2 1.1.4 2.3.6 3.6.6.6 0 1 .4 1 1V20c0 .6-.4 1-1 1A17 17 0 013 4c0-.6.4-1 1-1h3.5c.6 0 1 .4 1 1 0 1.3.2 2.5.6 3.6.1.3 0 .7-.2 1z"/></svg>
        </span>
        555-014-2290
      </p>
      <p class="contact__line contact__email">
        <span class="contact__icon">
          <svg width="15" height="15" viewBox="0 0 24 24" aria-hidden="true"><rect x="3" y="6" width="18" height="12" fill="none" stroke="#fff" stroke-width="2"/><path d="M3 6l9 7 9-7" fill="none" stroke="#fff" stroke-width="2"/></svg>
        </span>
        d.orwell@tidewellseafoods.com
      </p>
    </div>
    <div class="brand brand--front">
      <span class="brand__dot"></span>
      <span class="brand__name">Tidewell Seafoods</span>
    </div>
  </section>

  <section class="card card--back" aria-label="Business card back">
    <svg class="back-shape" viewBox="0 0 400 700" aria-hidden="true">
      <path d="M70 0 H400 V330 C400 150 260 20 70 0 Z" fill="var(--brand-blue)"/>
    </svg>
    <div class="brand brand--back">
      <span class="brand__dot"></span>
      <span class="brand__name">Tidewell Seafoods</span>
    </div>
  </section>
</main>
</body>
</html>
```